Business Cards/Stationary/Letterhead for Crestline Weight Loss Center
Be Healthy, Be Fit, and Be Ready to Lose Weight!
Creative Brief
Simple
Derek Tolsan, PA
Physician Assistant, Co-founder
52816 Birchwood Lane Fremont, CA 94592-7731
CrestlineSlim@mailhaven.example
www.crestlineslim.example
Aim for Results with Crestline Weight Loss! HCG, Appetite Suppressants,B12/B-Complex injections, Menu Plans, Exercise Plans, Nutriceuticals, Supplements.
Present this card to a friend; If your friend signs up, you will receive a 20% discount. The referrals are endless. If you refer 5 friends who sign up then you will receive 100% discount on your next visit. Just make sure your friend puts your name down in the "referral" section of the information sheet and you will be that much closer to saving. (Discount will only apply to weight loss program, discount only applicable for one month or week supply of medication. Non-transferrable. Referral cannot be an existing patient.) Appointment Date: _________ Time: _____

```html
<!DOCTYPE html>
<html lang="en">
<head>
<meta charset="utf-8">
<title>Crestline Weight Loss Center – Stationery</title>
<link href="https://fonts.googleapis.com/css2?family=Open+Sans:wght@400;600;700&display=swap" rel="stylesheet">
<style>
  :root {
    --green: #7db43f;
    --green-dark: #5f9a2c;
    --orange: #e8752b;
    --ink: #5a5a5a;
    --paper: #ffffff;
    --frame: #d9d9d9;
    --stage: #ffffff;
    --shadow: rgba(0,0,0,0.28);
  }
  * { box-sizing: border-box; margin: 0; padding: 0; }
  html, body { width: 1200px; height: 681px; overflow: hidden; background: var(--stage); }
  body { font-family: "Open Sans", Arial, sans-serif; color: var(--ink); position: relative; }

  .presentation-frame {
    position: absolute; left: 22px; top: 18px; width: 1156px; height: 636px;
    border: 2px solid var(--frame); background: var(--paper);
  }

  .sheet { position: absolute; background: var(--paper); box-shadow: 3px 5px 9px var(--shadow); overflow: hidden; }

  /* brand mark: name set in text with one plain circle */
  .brand { display: flex; align-items: center; gap: 6px; }
  .brand-dot { border-radius: 50%; background: var(--orange); flex: none; }
  .brand-name { color: var(--green); font-weight: 600; white-space: nowrap; }
  .brand-tagline { color: var(--green-dark); font-size: 5px; letter-spacing: .2px; margin-top: 2px; }

  .contact { text-align: center; color: var(--ink); line-height: 1.45; }

  .band { position: absolute; left: 0; right: 0; bottom: 0; display: flex; }
  .band-green { flex: 1; background: var(--green); }
  .band-orange { background: var(--orange); display: flex; align-items: center; justify-content: space-between; padding: 0 4px; }
  .band-square { width: 5px; height: 5px; background: #fff; opacity: .85; }

  /* envelope front */
  .envelope-front { left: 72px; top: 101px; width: 456px; height: 216px; }
  .envelope-front .brand { position: absolute; left: 12px; top: 18px; }
  .envelope-front .brand-dot { width: 22px; height: 22px; }
  .envelope-front .brand-name { font-size: 12px; }
  .envelope-front .contact { position: absolute; left: 0; right: 0; bottom: 26px; font-size: 6px; }
  .envelope-front .band { height: 11px; }
  .envelope-front .band-orange { width: 96px; }

  /* envelope back */
  .envelope-back { left: 72px; top: 360px; width: 456px; height: 216px; }
  .envelope-back svg.flap { position: absolute; left: 0; top: 0; }
  .envelope-back .seal-mark { position: absolute; left: 50%; top: 40px; transform: translateX(-50%); }
  .envelope-back .brand-dot { width: 26px; height: 26px; }

  /* letterhead */
  .letterhead { left: 619px; top: 43px; width: 317px; height: 581px; }
  .letterhead .masthead { position: absolute; left: 0; right: 0; top: 32px; display: flex; flex-direction: column; align-items: center; }
  .letterhead .brand-dot { width: 26px; height: 26px; }
  .letterhead .brand-name { font-size: 14px; }
  .letterhead .watermark-art {
    position: absolute; left: 88px; top: 176px; width: 150px; height: 240px; border-radius: 50% / 46%;
    background: radial-gradient(ellipse at 50% 45%, rgba(232,117,43,.16) 0%, rgba(125,180,63,.10) 55%, rgba(125,180,63,.04) 100%);
  }
  .letterhead .contact { position: absolute; left: 0; right: 0; bottom: 24px; font-size: 6px; }
  .letterhead .band { height: 11px; }
  .letterhead .band-orange { width: 70px; }

  /* business card front */
  .card-front { left: 960px; top: 197px; width: 158px; height: 105px; }
  .card-front .brand { position: absolute; left: 6px; top: 10px; gap: 3px; }
  .card-front .brand-dot { width: 11px; height: 11px; }
  .card-front .brand-name { font-size: 6.5px; }
  .card-front .person { position: absolute; right: 8px; top: 40px; width: 80px; text-align: center; }
  .card-front .person-name { font-size: 6px; font-weight: 600; color: var(--ink); }
  .card-front .person-role { font-size: 4.2px; color: var(--ink); margin-top: 1px; }
  .card-front .contact { position: absolute; left: 0; right: 0; bottom: 10px; font-size: 4px; }
  .card-front .band { height: 5px; }
  .card-front .band-orange { width: 34px; padding: 0 2px; }
  .card-front .band-square { width: 2px; height: 2px; }

  /* business card back */
  .card-back { left: 960px; top: 317px; width: 158px; height: 105px; background: var(--green); }
  .card-back .referral { position: absolute; left: 10px; right: 10px; top: 10px; color: #fff; font-size: 3.4px; line-height: 1.5; text-align: center; }
  .card-back .appointment { margin-top: 5px; font-size: 4px; font-weight: 600; }
</style>
</head>
<body>
<div class="presentation-frame"></div>

<section class="sheet envelope-front">
  <div class="brand">
    <span class="brand-dot"></span>
    <div>
      <div class="brand-name">Crestline Weight Loss Center</div>
      <div class="brand-tagline">Be Healthy, Be Fit, and Be Ready to Lose Weight!</div>
    </div>
  </div>
  <div class="contact">
    52816 Birchwood Lane | Fremont, CA 94592-7731<br>
    Phone: (510) 555-0148 | CrestlineSlim@mailhaven.example | www.crestlineslim.example
  </div>
  <div class="band">
    <span class="band-green"></span>
    <span class="band-orange"><i class="band-square"></i><i class="band-square"></i></span>
    <span class="band-green"></span>
  </div>
</section>

<section class="sheet envelope-back">
  <svg class="flap" width="456" height="216" viewBox="0 0 456 216" aria-hidden="true">
    <polyline points="2,2 228,112 454,2" fill="none" stroke="#8a8a8a" stroke-width="1"/>
  </svg>
  <div class="seal-mark"><span class="brand-dot" style="display:block"></span></div>
</section>

<section class="sheet letterhead">
  <header class="masthead">
    <span class="brand-dot"></span>
    <div class="brand-name" style="margin-top:6px">Crestline Weight Loss Center</div>
    <div class="brand-tagline">Be Healthy, Be Fit, and Be Ready to Lose Weight!</div>
  </header>
  <div class="watermark-art" role="img" aria-label="Faint decorative emblem with a raised-arms figure"></div>
  <footer class="contact">
    52816 Birchwood Lane | Fremont, CA 94592-7731<br>
    Phone: (510) 555-0148 | CrestlineSlim@mailhaven.example | www.crestlineslim.example
  </footer>
  <div class="band">
    <span class="band-green"></span>
    <span class="band-orange"><i class="band-square"></i><i class="band-square"></i></span>
    <span class="band-green"></span>
  </div>
</section>

<section class="sheet card-front">
  <div class="brand">
    <span class="brand-dot"></span>
    <div class="brand-name">Crestline Weight Loss Center</div>
  </div>
  <div class="person">
    <div class="person-name">Derek Tolsan, PA</div>
    <div class="person-role">Physician Assistant, Co-founder</div>
  </div>
  <div class="contact">
    52816 Birchwood Lane | Fremont, CA 94592-7731<br>
    (510) 555-0148 | CrestlineSlim@mailhaven.example<br>
    www.crestlineslim.example
  </div>
  <div class="band">
    <span class="band-green"></span>
    <span class="band-orange"><i class="band-square"></i><i class="band-square"></i></span>
    <span class="band-green"></span>
  </div>
</section>

<section class="sheet card-back">
  <div class="referral">
    Present this card to a friend; If your friend signs up, you will receive a 20% discount. The referrals are endless. If you refer 5 friends who sign up then you will receive 100% discount on your next visit. Just make sure your friend puts your name down in the "referral" section of the information sheet and you will be that much closer to saving. (Discount will only apply to weight loss program, discount only applicable for one month or week supply of medication. Non-transferrable. Referral cannot be an existing patient.)
    <div class="appointment">Appointment Date: _________ Time: _____</div>
  </div>
</section>
</body>
</html>
```